FLX & Harwick Solutions Business Card Design

a specialised consulting company, aviation specialist, like to have use blue colour on white background.
back of card to have printed-
NDT Expertise:
INSPECTION & TESTING CONSULTING
TRAINING & EDUCATION
CERTIFICATION SERVICES
LEVEL 3 SERVICES
VORTEM / AUDITING
INSPECTION SYSTEMS

Target Market(s)

Mainly the aerospace industry, manufacturers and airframe/engine overhaul companies.

Industry/Entity Type

Business

Contact Information for Business Card

FLX & Harwick Solutions

Derek Lomaxe JP

+61 (0)491570147
flxharwicksolutions@mailbox-demo.net

Font styles to use
Serif

Colors
3276b4
32a5d5

Requirements
Must have
• aviation style logo with letters FHS part of or adjacent to.

then company name: FLX & Harwick Solutions

then name in slightly smaller font : Derek Lomaxe JP

then phone and email details

Back of card, as per brief, but all text to be centred

```html
<!DOCTYPE html>
<html lang="en">
<head>
<meta charset="utf-8">
<title>FLX &amp; Harwick Solutions – Business Card</title>
<link rel="stylesheet" href="https://fonts.googleapis.com/css2?family=Tinos:wght@400;700&family=Arimo:wght@400&display=swap">
<style>
  :root {
    --brand-blue: #2a76b7;
    --brand-sky: #32a5d5;
    --map-light: #a9d6f2;
    --ink: #111111;
    --paper: #ffffff;
    --stage-center: #f2f3f4;
    --stage-edge: #c4c6c9;
    --divider: #e4e6e8;
  }
  * { margin: 0; padding: 0; box-sizing: border-box; }
  html, body { width: 1200px; height: 1200px; overflow: hidden; }
  body {
    background: radial-gradient(circle at 50% 50%, var(--stage-center) 0%, var(--stage-edge) 100%);
    position: relative;
    font-family: "Tinos", "Times New Roman", serif;
  }
  .card {
    position: absolute;
    left: 216px;
    width: 766px;
  }
  .card-front { top: 130px; height: 462px; }
  .card-back { top: 600px; height: 462px; }

  .front-top {
    position: absolute; left: 0; top: 0; width: 100%; height: 276px;
    background: var(--paper);
  }
  .world-map {
    position: absolute; left: 372px; top: 8px; width: 384px; height: 228px;
    background: radial-gradient(ellipse at 55% 45%, var(--map-light) 0%, rgba(169,214,242,0.35) 70%, rgba(169,214,242,0) 100%);
  }
  .brand-mark {
    position: absolute;
    font-family: "Tinos", "Times New Roman", serif;
    font-weight: 700;
    font-size: 50px;
    letter-spacing: 1px;
    line-height: 1;
  }
  .front-top .brand-mark { left: 198px; top: 86px; color: var(--brand-blue); }
  .company-name {
    position: absolute; left: 0; top: 150px; width: 100%;
    text-align: center;
    font-weight: 700; font-size: 36px; color: var(--ink);
    text-transform: uppercase;
  }
  .front-band {
    position: absolute; left: 0; top: 276px; width: 100%; height: 186px;
    background: var(--brand-blue); color: var(--paper);
  }
  .person-name {
    position: absolute; left: 0; top: 62px; width: 100%;
    text-align: center; font-weight: 700; font-size: 27px;
  }
  .contact {
    position: absolute; top: 134px;
    display: flex; align-items: center; gap: 8px;
    font-size: 21px;
  }
  .contact svg { width: 24px; height: 24px; flex: none; }
  .contact-phone { left: 26px; }
  .contact-email { left: 378px; }

  .back-band {
    position: absolute; left: 0; top: 0; width: 100%; height: 182px;
    background: var(--brand-blue);
  }
  .back-band .brand-mark { left: 0; width: 100%; text-align: center; top: 80px; color: var(--paper); }
  .back-body {
    position: absolute; left: 0; top: 182px; width: 100%; height: 280px;
    background: var(--paper); text-align: center; color: var(--ink);
  }
  .expertise-title { margin-top: 20px; font-weight: 700; font-size: 27px; }
  .expertise-list { list-style: none; margin-top: 12px; font-family: "Arimo", Arial, sans-serif; font-size: 18.5px; }
  .expertise-list li { line-height: 31px; }
</style>
</head>
<body>
  <section class="card card-front">
    <div class="front-top">
      <div class="world-map" role="img" aria-label="Dotted world map in light blue"></div>
      <div class="brand-mark">FHS</div>
      <h1 class="company-name">FLX &amp; Harwick Solutions</h1>
    </div>
    <div class="front-band">
      <p class="person-name">Derek Lomaxe JP</p>
      <p class="contact contact-phone">
        <svg viewBox="0 0 24 24" aria-hidden="true"><circle cx="12" cy="12" r="11" fill="#fff"/><path d="M8 6.5c.6-.4 1.2-.3 1.5.2l1.1 1.9c.3.5.2 1-.2 1.3l-.8.6c.6 1.4 1.6 2.5 3 3.1l.6-.8c.3-.4.9-.5 1.3-.2l1.9 1.1c.5.3.6.9.2 1.5-.8 1.2-2.2 1.6-3.6.9-2.6-1.2-4.5-3.2-5.6-5.7-.6-1.4-.3-2.9.6-3.9z" fill="var(--brand-blue)"/></svg>
        +61 (0)491570147
      </p>
      <p class="contact contact-email">
        <svg viewBox="0 0 24 24" aria-hidden="true"><circle cx="12" cy="12" r="11" fill="#fff"/><rect x="6" y="8" width="12" height="8.5" rx="1" fill="none" stroke="var(--brand-blue)" stroke-width="1.4"/><path d="M6.5 8.6 12 13l5.5-4.4" fill="none" stroke="var(--brand-blue)" stroke-width="1.4"/></svg>
        flxharwicksolutions@mailbox-demo.net
      </p>
    </div>
  </section>

  <section class="card card-back">
    <div class="back-band">
      <div class="brand-mark">FHS</div>
    </div>
    <div class="back-body">
      <h2 class="expertise-title">NDT Expertise:</h2>
      <ul class="expertise-list">
        <li>INSPECTION &amp; TESTING CONSULTING</li>
        <li>TRAINING &amp; EDUCATION</li>
        <li>CERTIFICATION SERVICES</li>
        <li>LEVEL 3 SERVICES</li>
        <li>VORTEM / AUDITING</li>
        <li>INSPECTION SYSTEMS</li>
      </ul>
    </div>
  </section>
</body>
</html>
```